KV HOLDING Business Cards

I need business cards for "KV Holding group LLC" doublesided... logo on the back (also include logo on front)
logo attached to project... i have jpg up..
Company Info:
418 East Marlow Avenue, Suite 7B
Chicago, Illinois 60617
facsimile 312-555-0188 (list fax, address, website on all cards.)
www.kvholdinggroup.example
Three different people on cards:
Dorian P. Kell, CPA MST
Principal
ofc 312-555-0142
mobile 312-555-0167
dorianpkell@kvholdinggroup.example
Marcus T. Brenholt, CPA MST
Principal
marcustbrenholt@kvholdinggroup.example
mobile 708-555-0119
ofc 312-555-0142
Nigel F Carrow
Principal
ofc 312-555-0142
no mobile
nigelfcarrow@kvholdinggroup.example
I have multiple projects listed.. see below:
Business cards for amber gate equity llc
letterhead
envelopes
Business cards for KV Holding LLC
letterhead
envelopes
Target Market(s)
rich people
Industry/Entity Type
Business
Look and feel

```html
<!DOCTYPE html>
<html lang="en">
<head>
<meta charset="utf-8">
<title>KV Holding Group LLC — Business Cards</title>
<link rel="stylesheet" href="https://fonts.googleapis.com/css2?family=Exo+2:wght@500;600&display=swap">
<style>
  :root {
    --navy: #0d3d73;
    --navy-dark: #0b3566;
    --paper: #ffffff;
    --band: #a9a9a9;
    --ink-light: #ffffff;
    --shadow: rgba(0, 0, 0, 0.45);
  }
  * { box-sizing: border-box; margin: 0; padding: 0; }
  html, body { width: 924px; height: 1200px; overflow: hidden; background: var(--paper); }
  body { position: relative; font-family: "Exo 2", sans-serif; }

  .card { position: absolute; box-shadow: 6px 8px 10px var(--shadow); overflow: hidden; background: var(--paper); }

  /* Front */
  .card-front { left: 64px; top: 87px; width: 789px; height: 485px; display: flex; }
  .front-brand { width: 395px; height: 100%; position: relative; color: var(--navy); text-align: center; }
  .front-contacts { flex: 1; background: var(--navy); color: var(--ink-light); text-align: center; font-weight: 600; position: relative; }

  .mark-dot { display: block; margin: 0 auto; border-radius: 50%; background: var(--navy); }
  .front-brand .mark-dot { position: absolute; left: 50%; top: 110px; width: 90px; height: 90px; margin-left: -45px; }
  .wordmark { font-family: "Exo 2", sans-serif; font-weight: 500; color: var(--navy); white-space: nowrap; letter-spacing: 0.5px; }
  .front-brand .wordmark { position: absolute; left: 0; right: 0; top: 222px; font-size: 27px; }

  .company-info { position: absolute; left: 0; right: 0; top: 292px; font-size: 12.5px; line-height: 18px; font-weight: 500; }

  .person { position: absolute; left: 0; right: 0; }
  .person-1 { top: 50px; font-size: 15px; line-height: 17.5px; }
  .person-2 { top: 200px; font-size: 13.5px; line-height: 16.5px; }
  .person-3 { top: 333px; font-size: 16px; line-height: 20px; }
  .person-3 .name { color: #e6edf5; }

  /* Back */
  .card-back { left: 74px; top: 607px; width: 779px; height: 474px; }
  .band { position: absolute; left: 0; right: 0; height: 93px; background: var(--band); }
  .band-top { top: 0; }
  .band-bottom { bottom: 0; }
  .back-brand { position: absolute; left: 0; right: 0; top: 93px; height: 288px; text-align: center; }
  .back-brand .mark-dot { position: absolute; left: 50%; top: 40px; width: 120px; height: 120px; margin-left: -60px; }
  .back-brand .wordmark { position: absolute; left: 0; right: 0; top: 203px; font-size: 38px; }
</style>
</head>
<body>

  <section class="card card-front">
    <div class="front-brand">
      <span class="mark-dot" aria-hidden="true"></span>
      <div class="wordmark">KV Holding Group LLC</div>
      <address class="company-info" style="font-style:normal">
        418 East Marlow Avenue, Suite 7B<br>
        Chicago, Illinois 60617<br>
        facsimile 312-555-0188 (list fax, address, website on all cards.)<br>
        www.kvholdinggroup.example
      </address>
    </div>
    <div class="front-contacts">
      <div class="person person-1">
        <div class="name">Dorian P. Kell, CPA MST</div>
        <div class="role">Principal</div>
        <div>Ofc 312-555-0142</div>
        <div>Mobile 312-555-0167</div>
        <div>dorianpkell@kvholdinggroup.example</div>
      </div>
      <div class="person person-2">
        <div class="name">Marcus T. Brenholt, CPA MST</div>
        <div class="role">Principal</div>
        <div>marcustbrenholt@kvholdinggroup.example</div>
        <div>mobile 708-555-0119</div>
        <div>ofc 312-555-0142</div>
      </div>
      <div class="person person-3">
        <div class="name">Nigel F Carrow</div>
        <div class="role">Principal</div>
        <div>ofc 312-555-0142</div>
        <div>nigelfcarrow@kvholdinggroup.example</div>
      </div>
    </div>
  </section>

  <section class="card card-back">
    <div class="band band-top"></div>
    <div class="back-brand">
      <span class="mark-dot" aria-hidden="true"></span>
      <div class="wordmark">KV Holding Group LLC</div>
    </div>
    <div class="band band-bottom"></div>
  </section>

</body>
</html>
```